refurbishment of diamond cut alloy wheels

we need to design a flyer that will catch the eye of the customer to refurbish diamond cut alloy wheels. we refurbish the wheels by using the latest CNC machine to precision cut and resurface the wheel. we would like before and after pictures of maybe Valtorin, KRZ, Ovel wheels to give it a prestige look. The final design should communicate an expensive look and providing a good image for the business. The colours that I would like to use is black and red which should make the flyer stand out. The logo must sit on a black background without the wordings of specialists in TQ, Ovel etc and also without servicing, diagnostics etc as well. This flyer is just to communicate refurbishment of alloy wheels to high standard.

Target Market(s)

any members of the public and car dealerships

Industry/Entity Type

Automotive

Colors

Designer to choose colors to be used in the design.

Requirements
Must have
• Wow factor with great images of wheels
Nice to have
• Maybe on the front of the flyer it has a picture of a wheel and then on the back of the flyer it has before and after pictures to show how just how incredible it is to refurbish wheels
Should not have
• other makes of wheels apart from KRZ, Ovel, and any other high end makes of vehicles wheels

```html
<!DOCTYPE html>
<html lang="en">
<head>
<meta charset="utf-8">
<title>Redline Motors – Wheel Refurbishment Flyer</title>
<link href="https://fonts.googleapis.com/css2?family=Russo+One&family=Open+Sans:wght@400;600&display=swap" rel="stylesheet">
<style>
  :root{
    --stage:#eef0f2;
    --ink:#0b0b0c;
    --red:#e3121b;
    --white:#ffffff;
    --muted:#d6d6d6;
    --rule:#3a3a3c;
    --display:"Russo One", sans-serif;
    --body:"Open Sans", sans-serif;
  }
  *{box-sizing:border-box;margin:0;padding:0}
  html,body{width:1200px;height:1200px;overflow:hidden;background:var(--stage)}
  .canvas{position:relative;width:1200px;height:1200px;display:flex;gap:40px;justify-content:center;align-items:center}
  .page{position:relative;width:540px;height:780px;background:radial-gradient(ellipse at 50% 40%,#262628 0%,var(--ink) 75%);color:var(--white);overflow:hidden;box-shadow:0 12px 30px rgba(0,0,0,.18)}

  /* front */
  .front-title{height:150px;background:var(--ink);display:flex;flex-direction:column;justify-content:center;align-items:center;font-family:var(--display);color:var(--red);line-height:1}
  .front-title .line-1{font-size:58px;letter-spacing:1px}
  .front-title .amp{font-size:26px;vertical-align:top}
  .front-title .line-2{font-size:40px;margin-top:6px}
  .hero-photo{height:380px;background:radial-gradient(circle at 45% 50%,#5a5a5e 0%,#2a2a2c 38%,#0e0e10 72%)}
  .front-copy{text-align:center;padding:26px 30px 0;font-family:var(--body);font-weight:600;font-size:17px;line-height:1.3;text-transform:uppercase}
  .front-copy .hl{color:var(--red)}
  .front-phone{font-family:var(--display);color:var(--red);font-size:30px;margin-top:6px}

  .brand{display:flex;align-items:center;gap:10px;justify-content:center;font-family:var(--display);color:var(--red);text-transform:uppercase;white-space:nowrap}
  .brand .mark{width:22px;height:22px;background:var(--red);flex:none}
  .front .brand{margin-top:28px;font-size:28px}

  /* back */
  .back{padding:24px 36px;display:flex;flex-direction:column}
  .back-title{font-family:var(--display);color:var(--red);font-size:24px;line-height:1.08;text-align:center;text-transform:uppercase}
  .intro{font-family:var(--body);font-size:11px;line-height:1.45;text-align:center;margin-top:12px;color:var(--muted)}
  .intro p+p{margin-top:8px}
  .compare{margin-top:14px;background:var(--white);padding:10px;display:flex;gap:10px}
  .compare figure{position:relative;flex:1;height:150px}
  .compare .photo{height:100%}
  .compare .before-photo{background:linear-gradient(160deg,#c9c9c9,#6c6a66 55%,#3a3836)}
  .compare .after-photo{background:radial-gradient(circle,#f0f0f0 0%,#bdbdc0 45%,#8b8a90 80%)}
  .compare figcaption{position:absolute;bottom:-6px;font-family:var(--display);font-size:13px;background:var(--red);color:var(--white);padding:2px 10px;text-transform:uppercase}
  .compare .before figcaption{left:0}
  .compare .after figcaption{right:0}
  .makes-title{font-family:var(--display);color:var(--red);font-size:15px;text-align:center;margin-top:18px;text-transform:uppercase}
  .makes{list-style:none;display:flex;flex-wrap:wrap;justify-content:center;gap:3px 16px;font-family:var(--body);font-size:11px;margin-top:6px}
  .makes li{display:flex;align-items:center;gap:4px}
  .tick{width:11px;height:11px}
  .contact{font-family:var(--body);font-size:11px;text-align:center;margin-top:10px;line-height:1.4;font-style:normal}
  .contact .icon{width:11px;height:11px;display:block;margin:6px auto 2px}
  .back-foot{display:flex;justify-content:space-between;align-items:center;margin-top:auto;border-top:1px solid var(--rule);padding-top:14px}
  .back .brand{font-size:21px}
  .phones{display:flex;align-items:center;gap:10px;font-family:var(--display);color:var(--red);font-size:19px;line-height:1.15;white-space:nowrap}
  .phones svg{width:26px;height:26px;flex:none}
</style>
</head>
<body>
<main class="canvas">

  <section class="page front">
    <header class="front-title">
      <div class="line-1">WHEELS <span class="amp">&amp;</span></div>
      <div class="line-2">REFURBISHMENTS</div>
    </header>
    <div class="hero-photo" role="img" aria-label="Close-up photograph of a dark multi-spoke alloy wheel with low-profile tyre"></div>
    <div class="front-copy">
      We now offer alloy <span class="hl">wheel refurbishments.</span><br>
      If your alloys need <span class="hl">refurbishment</span><br>
      contact us today
      <div class="front-phone">ON 01632 960 026</div>
    </div>
    <div class="brand"><span class="mark"></span>Redline Motors</div>
  </section>

  <section class="page back">
    <h1 class="back-title">Alloy refurbishment<br>specialists in and<br>around Eastford</h1>
    <div class="intro">
      <p>If you are looking to refresh the look of your car but don't want the expense of new alloys, with a wide range of limited edition colours to choose from why not consider customising and refurbishing your existing alloys?</p>
      <p>If you've had your alloy wheels long enough for them to require alloy refurbishment you can choose from a wide range of colours for refurbishment or choose a brand new set from our comprehensive range. At Apex Wheels &amp; Tyres, we stock an extensive range of the latest designs from all the leading suppliers and manufacturers so you are sure to find a stylish new design.</p>
    </div>
    <div class="compare">
      <figure class="before"><div class="photo before-photo" role="img" aria-label="Damaged silver alloy wheel with flat tyre before refurbishment"></div><figcaption>Before</figcaption></figure>
      <figure class="after"><div class="photo after-photo" role="img" aria-label="Refurbished silver alloy wheel after refurbishment"></div><figcaption>After</figcaption></figure>
    </div>
    <h2 class="makes-title">Cars we specialise in include:</h2>
    <ul class="makes">
      <li><svg class="tick" viewBox="0 0 12 12"><path d="M1 6l3 3 7-7" fill="none" stroke="#e3121b" stroke-width="2"/></svg>Ovel</li>
      <li><svg class="tick" viewBox="0 0 12 12"><path d="M1 6l3 3 7-7" fill="none" stroke="#e3121b" stroke-width="2"/></svg>Valtorin</li>
      <li><svg class="tick" viewBox="0 0 12 12"><path d="M1 6l3 3 7-7" fill="none" stroke="#e3121b" stroke-width="2"/></svg>Sorel</li>
      <li><svg class="tick" viewBox="0 0 12 12"><path d="M1 6l3 3 7-7" fill="none" stroke="#e3121b" stroke-width="2"/></svg>Kestra</li>
      <li><svg class="tick" viewBox="0 0 12 12"><path d="M1 6l3 3 7-7" fill="none" stroke="#e3121b" stroke-width="2"/></svg>TQ</li>
      <li><svg class="tick" viewBox="0 0 12 12"><path d="M1 6l3 3 7-7" fill="none" stroke="#e3121b" stroke-width="2"/></svg>Vehicles of all makes and models</li>
    </ul>
    <address class="contact">
      <svg class="icon" viewBox="0 0 12 12"><path d="M6 0a4 4 0 0 0-4 4c0 3 4 8 4 8s4-5 4-8a4 4 0 0 0-4-4z" fill="#e3121b"/><circle cx="6" cy="4" r="1.5" fill="#0b0b0c"/></svg>
      Redline Motors, 14 Larch Lane, Millbrook,<br>Eastford, Westshire, EF3 0AB
      <svg class="icon" viewBox="0 0 12 12"><rect x="0" y="2" width="12" height="8" rx="1" fill="#e3121b"/><path d="M0 3l6 4 6-4" fill="none" stroke="#0b0b0c"/></svg>
      info@redlinemotors.example
      <svg class="icon" viewBox="0 0 12 12"><circle cx="6" cy="6" r="5.5" fill="#e3121b"/></svg>
      www.redlinemotors.example
    </address>
    <div class="back-foot">
      <div class="brand"><span class="mark"></span>Redline Motors</div>
      <div class="phones">
        <svg viewBox="0 0 26 26"><circle cx="13" cy="13" r="13" fill="#e3121b"/><path d="M9 7l3 3-1.5 1.5c1 2 2 3 4 4L16 14l3 3-2 2c-5 0-10-5-10-10z" fill="#0b0b0c"/></svg>
        <div>01632 960 026<br>07700 900 427</div>
      </div>
    </div>
  </section>

</main>
</body>
</html>
```